Halvorn - Refresh the look and feel of an existing website

We currently have an existing website www.halvornworldadvisory.example however it needs a more refreshed 'look and feel'. We are a professional consultancy that works with large corporate organisations and government. Our 'tag line' is A New Way of Thinking. We want the site to communicate "Innovation" and Leading Edge Thinking.

Target Market(s)

Corporate and Professional Clients - Organisation and Business Change

Industry/Entity Type

Management Consulting

Number of Pages Required

1 page

Font styles to use
Sans Serif

Requirements
Must have
• Must have a professional Corporate look and feel. Header 'imagery' is ok but boxes on front page need changing ... along with the words. The focus on home page needs to 'call out' 3 main consulting areas:-
• - Change & Transformation Specialists
• - Innovative Solutions
• - Digital Transformation
• Tag Line for business is ... A New Way of Thinking (Highlighting Halvorn as 'Thought Leaders' in business)
Nice to have
• Less "words' more imagery. Possibly an area for a 'video' or recent articles/blogs on the front page. Needs to have more of an 'interactive' feel. We are open to suggestions.
Should not have
• NA

```html
<!DOCTYPE html>
<html lang="en">
<head>
<meta charset="utf-8">
<title>Halvorn Global Solutions</title>
<link href="https://fonts.googleapis.com/css2?family=Raleway:wght@200;300;400;600;700;800&family=Open+Sans:wght@400;600;700&display=swap" rel="stylesheet">
<style>
:root{
  --cyan:#3fc4de;
  --cyan-deep:#1fa6c6;
  --navy:#1c2b44;
  --navy-2:#2a3d5c;
  --ink:#2b2b2b;
  --body:#555b63;
  --grey:#ebebec;
  --card:#e6e6e7;
  --muted:#b9c4d3;
  --white:#ffffff;
}
*{margin:0;padding:0;box-sizing:border-box}
html,body{width:1200px;height:4100px;overflow:hidden;background:var(--white)}
body{position:relative;font-family:"Open Sans",Arial,sans-serif;color:var(--body)}
.abs{position:absolute}

/* header */
.hero-photo{left:0;top:0;width:1200px;height:740px;background:linear-gradient(110deg,#7fdcef 0%,#48c7e1 55%,#2bb3d4 100%);clip-path:polygon(0 0,1200px 0,1200px 600px,0 740px)}
.topbar{left:0;top:0;width:1200px;height:88px;background:var(--navy)}
.brand-plate{left:0;top:0;width:400px;height:108px;background:var(--white);clip-path:polygon(0 0,400px 0,360px 108px,0 108px)}
.brand{left:72px;top:22px;display:flex;align-items:center;gap:16px}
.brand-dot{width:62px;height:62px;border-radius:50%;background:var(--navy)}
.brand-name{font-family:"Raleway",sans-serif;font-weight:700;font-size:38px;letter-spacing:1px;color:var(--navy)}
.nav{left:432px;top:28px;display:flex;gap:30px;list-style:none}
.nav li{font-family:"Raleway",sans-serif;font-size:15px;font-weight:600;color:var(--white);text-transform:uppercase;letter-spacing:.3px}
.tagline{font-family:"Raleway",sans-serif;font-weight:200;color:var(--white);line-height:1;text-transform:uppercase}
.tag-a{left:392px;top:148px;font-size:140px}
.tag-new{left:238px;top:262px;font-size:150px;letter-spacing:-2px}
.tag-way{left:448px;top:340px;font-size:150px;letter-spacing:-2px}
.tag-think{left:462px;top:492px;font-size:86px;font-weight:300}
.btn{display:block;border:3px solid var(--cyan);border-radius:30px;font-family:"Raleway",sans-serif;font-weight:700;font-size:14px;color:var(--cyan-deep);text-transform:uppercase;text-align:center;letter-spacing:.5px}
.btn-hero{left:476px;top:600px;width:172px;height:46px;line-height:40px;border-color:var(--white);color:var(--white)}

/* welcome */
.welcome-bg{left:0;top:0;width:1200px;height:1080px}
.welcome-photo{left:540px;top:690px;width:660px;height:330px;background:linear-gradient(135deg,#b9c3cc,#6f7f90 60%,#4a5868);clip-path:polygon(0 0,660px 30px,660px 250px,0 330px)}
.welcome-label{left:118px;top:780px;font-family:"Raleway",sans-serif;font-weight:700;font-size:15px;color:var(--cyan-deep);text-transform:uppercase}
.welcome-title{left:118px;top:802px;font-family:"Raleway",sans-serif;font-weight:700;font-size:23px;color:var(--ink);text-transform:uppercase;letter-spacing:.3px}
.welcome-text{left:118px;top:850px;width:400px;font-size:15px;line-height:25px}
.btn-welcome{left:118px;top:942px;width:152px;height:44px;line-height:38px}

/* services */
.photo{background:linear-gradient(135deg,#d7dfe6,#9aa9b8)}
.svc-photo{width:422px;height:423px}
.svc-title{font-family:"Raleway",sans-serif;font-weight:800;font-size:33px;line-height:34px;color:#222;text-transform:uppercase;letter-spacing:.5px}
.svc-rule{height:3px;width:54px;background:var(--cyan)}
.svc-copy{width:330px}
.svc-text{font-size:13.5px;line-height:23px}
.svc-copy .btn{width:152px;height:44px;line-height:38px;margin-top:22px}
.quote-name{margin-top:18px;font-size:14px;font-weight:700;color:#333}
.dots{display:flex;gap:8px;margin-top:16px}
.dots span{width:11px;height:11px;border-radius:50%;background:#c9d6de}
.dots span:first-child{background:var(--cyan)}
.quote-title{left:649px;top:2116px;font-family:"Raleway",sans-serif;font-weight:800;font-size:22px;color:#222;text-transform:uppercase}

/* video */
.video{left:0;top:2536px;width:1200px;height:452px;background:linear-gradient(120deg,#142238 0%,#1e2f4a 50%,#102033 100%)}
.video-title{left:137px;top:2676px;font-family:"Raleway",sans-serif;font-weight:800;font-size:24px;color:var(--white);text-transform:uppercase}
.play{left:137px;top:2730px;display:flex;align-items:center;gap:18px;font-family:"Raleway",sans-serif;font-size:16px;color:#dfe5ee}
.play-line{display:inline-block;width:90px;height:1px;background:#9aa6b6}
.btn-video{left:137px;top:2808px;width:152px;height:44px;line-height:38px;border-color:var(--white);color:var(--white)}

/* blog */
.blog-head{left:0;top:3044px;width:1200px;text-align:center;font-family:"Raleway",sans-serif;font-weight:800;font-size:25px;color:#222;text-transform:uppercase}
.blog-sub{left:0;top:3086px;width:1200px;text-align:center;font-size:17px;color:#333}
.post{top:3151px;width:331px;height:443px;background:var(--card)}
.post .photo{height:252px}
.post-date{margin:20px 28px 0;font-size:13px;color:#555}
.post-title{margin:8px 28px 0;font-family:"Raleway",sans-serif;font-weight:700;font-size:17px;line-height:21px;color:#222}
.post-text{margin:10px 28px 0;font-size:12.5px;line-height:20px;color:#6a6e73}

/* footer */
.footer{left:0;top:3620px;width:1200px;height:480px}
.foot-brand{right:70px;top:3680px;display:flex;align-items:center;gap:12px}
.foot-brand .brand-dot{width:44px;height:44px;background:var(--white)}
.foot-brand .brand-name{font-size:26px;color:var(--white)}
.foot-h{font-family:"Raleway",sans-serif;font-weight:800;font-size:16px;color:var(--white);text-transform:uppercase}
.foot-list{list-style:none;margin-top:18px}
.foot-list li{font-size:14px;line-height:24px;color:var(--muted)}
.contact{display:flex;gap:14px;margin-top:16px}
.contact svg{flex:none;margin-top:2px}
.contact b{display:block;color:var(--white);font-size:13px}
.contact span{display:block;font-size:13px;color:var(--muted);line-height:20px}
.foot-note{margin-top:16px;font-size:13px;color:var(--muted)}
.subscribe{display:flex;align-items:center;gap:12px;margin-top:16px}
.subscribe .field{width:196px;height:40px;border-radius:20px;background:var(--white);font-size:12px;color:#999;padding:11px 18px}
.go{width:44px;height:44px;border-radius:50%;border:3px solid var(--cyan);display:flex;align-items:center;justify-content:center}
.copyright{left:74px;top:4058px;font-size:13px;color:var(--muted)}
.social{left:970px;top:4044px;display:flex;gap:8px}
.social span{width:34px;height:34px;border-radius:50%;border:2px solid var(--white)}
</style>
</head>
<body>

<!-- Header -->
<div class="abs hero-photo" role="img" aria-label="Photo of two colleagues collaborating at a desk with a cyan colour overlay"></div>
<div class="abs topbar"></div>
<div class="abs brand-plate"></div>
<div class="abs brand"><span class="brand-dot"></span><span class="brand-name">HALVORN</span></div>
<ul class="abs nav">
  <li>Home</li><li>About Us</li><li>Our Services</li><li>Solutions</li><li>What's Happening</li><li>Contact Us</li>
</ul>
<h1>
  <span class="abs tagline tag-a">A</span>
  <span class="abs tagline tag-new">New</span>
  <span class="abs tagline tag-way">Way</span>
  <span class="abs tagline tag-think">Of Thinking</span>
</h1>
<a class="abs btn btn-hero">Learn More</a>

<!-- Welcome -->
<svg class="abs welcome-bg" width="1200" height="1080" viewBox="0 0 1200 1080" aria-hidden="true">
  <polygon points="0,740 1200,600 1200,1000 0,1064" fill="#ebebec"/>
  <polygon points="0,1064 1200,920 1200,1080 0,1080" fill="#ffffff"/>
</svg>
<div class="abs welcome-photo" role="img" aria-label="Photo of a business meeting around a conference table"></div>
<p class="abs welcome-label">Welcome to</p>
<h2 class="abs welcome-title">Halvorn Global Solutions</h2>
<p class="abs welcome-text">Our strength is our people - highly skilled, dedicated specialists who have proven experience delivering the outcomes that our clients need.</p>
<a class="abs btn btn-welcome">Learn More</a>

<!-- Service: Change & Transformation -->
<div class="abs photo svc-photo" role="img" aria-label="Photo of two business people stacking blocks together" style="left:118px;top:1140px;background:linear-gradient(135deg,#e8eef3,#b8c6d2 55%,#8d9aa7)"></div>
<h3 class="abs svc-title" style="left:136px;top:1510px">Change &amp;<br>Transformation<br>Specialists</h3>
<div class="abs svc-rule" style="left:136px;top:1626px"></div>
<div class="abs svc-copy" style="left:200px;top:1616px">
  <p class="svc-text">Lorem ipsum dolor sit amet, consectetur adipiscing elit, sed do eiusmod tempor incididunt ut labore et dolore magna aliqua. Ut enim ad minim veniam, quis nostrud exercitation ullamco laboris nisi ut aliquip ex ea commodo.</p>
  <a class="btn">Learn More</a>
</div>

<!-- Service: Digital Transformation -->
<div class="abs photo svc-photo" role="img" aria-label="Photo of a businessman holding a glowing tablet showing a world map" style="left:631px;top:1353px;background:linear-gradient(160deg,#9aa4ad,#4e5a66 50%,#2b6f8f)"></div>
<h3 class="abs svc-title" style="left:649px;top:1724px">Digital<br>Transformation</h3>
<div class="abs svc-rule" style="left:649px;top:1806px"></div>
<div class="abs svc-copy" style="left:713px;top:1796px">
  <p class="svc-text">Lorem ipsum dolor sit amet, consectetur adipiscing elit, sed do eiusmod tempor incididunt ut labore et dolore magna aliqua. Ut enim ad minim veniam, quis nostrud exercitation ullamco laboris nisi ut aliquip ex ea commodo.</p>
  <a class="btn">Learn More</a>
</div>

<!-- Service: Innovative Solutions -->
<div class="abs photo svc-photo" role="img" aria-label="Illustration of a thoughtful woman beneath sketched ideas and a rocket" style="left:118px;top:1848px;height:422px;background:linear-gradient(135deg,#f1f1f1,#d6d6d6 60%,#b9b9b9)"></div>
<h3 class="abs svc-title" style="left:136px;top:2216px">Innovative<br>Solutions</h3>
<div class="abs svc-rule" style="left:136px;top:2302px"></div>
<div class="abs svc-copy" style="left:200px;top:2292px">
  <p class="svc-text">Lorem ipsum dolor sit amet, consectetur adipiscing elit, sed do eiusmod tempor incididunt ut labore et dolore magna aliqua. Ut enim ad minim veniam, quis nostrud exercitation ullamco laboris nisi ut aliquip ex ea commodo.</p>
  <a class="btn">Learn More</a>
</div>

<!-- Testimonial -->
<h3 class="abs quote-title">Why Client Love Us?</h3>
<div class="abs svc-rule" style="left:649px;top:2172px"></div>
<div class="abs svc-copy" style="left:713px;top:2162px">
  <p class="svc-text">Lorem ipsum dolor sit amet, consectetur adipiscing elit, sed do eiusmod tempor incididunt ut labore et dolore magna aliqua. Ut enim ad minim veniam, quis nostrud exercitation ullamco laboris nisi ut aliquip ex ea commodo.</p>
  <p class="quote-name">Marcus Ellery</p>
  <div class="dots"><span></span><span></span><span></span><span></span><span></span></div>
</div>

<!-- Video -->
<div class="abs video" role="img" aria-label="Photo of a team working together on laptops in a dark office"></div>
<h2 class="abs video-title">Whach Our Video</h2>
<div class="abs play">
  <svg width="44" height="44" viewBox="0 0 44 44" aria-hidden="true"><circle cx="22" cy="22" r="20" fill="none" stroke="#fff" stroke-width="3"/><polygon points="17,13 31,22 17,31" fill="#fff"/></svg>
  <span class="play-line"></span>
  <span>Play</span>
</div>
<a class="abs btn btn-video">Learn More</a>

<!-- Blog -->
<h2 class="abs blog-head">Blog Posts</h2>
<p class="abs blog-sub">Lorem ipsum copy in various charsets and languages for layouts.</p>

<article class="abs post" style="left:74px">
  <div class="photo" role="img" aria-label="Photo of two colleagues smiling at a laptop" style="background:linear-gradient(135deg,#e4e9ee,#aab5bf)"></div>
  <p class="post-date">January 27, 2016</p>
  <h4 class="post-title">Lorem ipsum dolor sit amet, consectetur adipiscing elit</h4>
  <p class="post-text">sed do eiusmod tempor incididunt ut labore et dolore magna aliqua. Ut enim ad minim veniam, quis nostrud exercitation.</p>
</article>
<article class="abs post" style="left:435px">
  <div class="photo" role="img" aria-label="Photo of a team meeting around laptops" style="background:linear-gradient(135deg,#bcc5cc,#6f7b86)"></div>
  <p class="post-date">January 24, 2016</p>
  <h4 class="post-title">Lorem ipsum dolor sit amet, consectetur adipiscing elit</h4>
  <p class="post-text">sed do eiusmod tempor incididunt ut labore et dolore magna aliqua. Ut enim ad minim veniam, quis nostrud exercitation.</p>
</article>
<article class="abs post" style="left:795px">
  <div class="photo" role="img" aria-label="Photo of two men discussing work at a laptop" style="background:linear-gradient(135deg,#d5dbe2,#7d8c9c)"></div>
  <p class="post-date">November 3, 2015</p>
  <h4 class="post-title">Lorem ipsum dolor sit amet, consectetur adipiscing elit</h4>
  <p class="post-text">sed do eiusmod tempor incididunt ut labore et dolore magna aliqua. Ut enim ad minim veniam, quis nostrud exercitation.</p>
</article>

<!-- Footer -->
<svg class="abs footer" width="1200" height="480" viewBox="0 0 1200 480" aria-hidden="true">
  <polygon points="0,40 560,40 760,0 1200,0 1200,480 0,480" fill="#2a3d5c"/>
  <polygon points="0,120 1200,70 1200,480 0,480" fill="#1c2b44"/>
</svg>
<div class="abs foot-brand"><span class="brand-dot"></span><span class="brand-name">HALVORN</span></div>

<div class="abs" style="left:74px;top:3780px">
  <h5 class="foot-h">About Us</h5>
  <ul class="foot-list"><li>Our Team</li><li>Our Values</li><li>Giving Back</li></ul>
</div>
<div class="abs" style="left:344px;top:3780px">
  <h5 class="foot-h">Our Services</h5>
  <ul class="foot-list"><li>Strategy and Design</li><li>Transformation</li><li>Change &amp; Culture</li><li>Organisational Development</li><li>Project Management</li><li>Organisational Efficiency</li><li>Specialist Placements</li></ul>
</div>
<div class="abs" style="left:612px;top:3780px">
  <h5 class="foot-h">Get In Touch</h5>
  <div class="contact">
    <svg width="16" height="16" viewBox="0 0 16 16" aria-hidden="true"><path d="M3 1l3 3-2 2c1 2 3 4 5 5l2-2 3 3-2 3C6 15 1 10 1 3z" fill="#fff"/></svg>
    <div><b>AUS</b><span>1300 555 019 (AUS)</span><b style="margin-top:8px">NZ</b><span>0800 555 027 (NZ)</span><b style="margin-top:8px">INTL</b><span>1300 555 019</span></div>
  </div>
  <div class="contact" style="margin-top:14px">
    <svg width="16" height="12" viewBox="0 0 16 12" aria-hidden="true"><rect x="0.5" y="0.5" width="15" height="11" fill="#fff"/><path d="M1 1l7 6 7-6" stroke="#1c2b44" stroke-width="1.5" fill="none"/></svg>
    <span>info@halvornworldadvisory.example</span>
  </div>
</div>
<div class="abs" style="left:883px;top:3780px">
  <h5 class="foot-h">Stay Informed</h5>
  <p class="foot-note">Get news, views, insight and events</p>
  <div class="subscribe">
    <div class="field">Enter email address</div>
    <div class="go"><svg width="16" height="16" viewBox="0 0 16 16" aria-hidden="true"><path d="M5 2l6 6-6 6" stroke="#3fc4de" stroke-width="3" fill="none"/></svg></div>
  </div>
</div>

<p class="abs copyright">Copyright © 2016 Halvorn Global Solutions</p>
<div class="abs social"><span></span><span></span><span></span><span></span></div>

</body>
</html>
```